Pest Control Company needs business card!

Hi there, we need a business card designed for our new Pest Control Company. Ideally this card will be simple, yet feel elegant and high end. We want to use the colours Orange, Black and White. Please see our attached logo for the exact colours.

Business card details:

Phone - 0461 275 804
Name - Gavin Holloway
Email - Info@steadfastverminguard.com.au

We would also like to include the following list with dot points:

SERVICES / INSPECTIONS

Termites, Wood Borers, Ants, Cockroaches, Spiders, Fleas, Mice, Rats, Bed Bugs, & More!

```html
<!DOCTYPE html>
<html lang="en">
<head>
<meta charset="utf-8">
<title>Steadfast Vermin Guard – Business Card</title>
<link href="https://fonts.googleapis.com/css2?family=Oswald:wght@400;500&family=PT+Sans:wght@400;700&display=swap" rel="stylesheet">
<style>
  :root {
    --ink: #231f20;
    --yellow: #fed50f;
    --orange: #f28c1e;
    --orange-deep: #e0761a;
    --grey: #b9b9b9;
    --list: #d9d9d9;
    --backdrop: #8fb4bd;
  }
  html, body {
    margin: 0;
    width: 1200px;
    height: 800px;
    overflow: hidden;
    background: var(--backdrop);
  }
  .card {
    position: absolute;
    left: 395px;
    width: 414px;
    height: 237px;
    background: var(--ink);
    overflow: hidden;
  }
  .card--front { top: 119px; }
  .card--back { top: 430px; }
  .card__shapes {
    position: absolute;
    inset: 0;
    width: 100%;
    height: 100%;
  }
  .brand {
    position: absolute;
    display: flex;
    align-items: center;
    gap: 6px;
    font-family: "Oswald", sans-serif;
    font-weight: 500;
    text-transform: uppercase;
    line-height: 1;
  }
  .brand__name { display: flex; flex-direction: column; }
  .brand__mark { border-radius: 50%; flex: none; }
  .brand--front {
    left: 139px;
    top: 82px;
    color: var(--orange);
    font-size: 19px;
    letter-spacing: 0.5px;
  }
  .brand--front .brand__mark { width: 22px; height: 22px; background: var(--orange); }
  .brand--back {
    left: 329px;
    top: 27px;
    color: var(--ink);
    font-size: 8px;
    letter-spacing: 0.2px;
  }
  .brand--back .brand__mark { width: 12px; height: 12px; background: var(--ink); gap: 3px; }
  .holder {
    position: absolute;
    left: 65px;
    top: 50px;
    margin: 0;
    font-family: "Oswald", sans-serif;
    font-weight: 500;
    font-size: 20px;
    letter-spacing: 0.3px;
    text-transform: uppercase;
  }
  .holder__first { color: var(--orange); }
  .holder__last { color: var(--grey); }
  .contact {
    position: absolute;
    display: flex;
    align-items: center;
    gap: 5px;
    font-family: "PT Sans", sans-serif;
    font-size: 10px;
    color: var(--yellow);
  }
  .contact svg { width: 7px; height: 7px; }
  .contact--phone { left: 93px; top: 104px; }
  .contact--email { left: 105px; top: 126px; }
  .services {
    position: absolute;
    left: 0;
    right: 0;
    top: 190px;
    margin: 0;
    padding-left: 76px;
    text-align: center;
    font-family: "PT Sans", sans-serif;
    font-size: 9.5px;
    line-height: 13.5px;
    color: var(--list);
    word-spacing: 1px;
  }
  .services .sep { margin: 0 5px; }
</style>
</head>
<body>

<section class="card card--front" aria-label="Card front">
  <svg class="card__shapes" viewBox="0 0 812 464" preserveAspectRatio="none" aria-hidden="true">
    <defs>
      <linearGradient id="band-left" x1="0" y1="0" x2="1" y2="0">
        <stop offset="0" stop-color="var(--orange-deep)"/>
        <stop offset="1" stop-color="var(--orange)"/>
      </linearGradient>
    </defs>
    <path d="M0,130 L28,130 Q60,130 78,160 L205,380 Q222,410 205,440 L192,464 L0,464 Z" fill="url(#band-left)"/>
    <path d="M0,158 L28,158 Q48,158 62,182 L180,390 Q192,412 180,434 L163,464 L0,464 Z" fill="var(--yellow)"/>
    <path d="M547,0 L812,0 L812,238 L720,238 Q682,238 660,205 Z" fill="var(--orange)"/>
    <path d="M580,0 L812,0 L812,209 L742,209 Q712,209 695,182 Z" fill="var(--yellow)"/>
  </svg>
  <div class="brand brand--front">
    <span class="brand__name"><span>Steadfast</span><span>Vermin</span><span>Guard</span></span>
    <span class="brand__mark"></span>
  </div>
</section>

<section class="card card--back" aria-label="Card back">
  <svg class="card__shapes" viewBox="0 0 812 464" preserveAspectRatio="none" aria-hidden="true">
    <path d="M0,135 Q20,145 32,165 L150,380 Q168,410 152,440 L140,464 L0,464 Z" fill="var(--orange)"/>
    <path d="M0,178 L126,392 Q138,412 126,434 L111,464 L0,464 Z" fill="var(--yellow)"/>
    <path d="M473,0 L812,0 L812,186 L652,186 Q612,186 590,150 Z" fill="var(--orange)"/>
    <path d="M508,0 L812,0 L812,157 L664,157 Q634,157 614,125 Z" fill="var(--yellow)"/>
  </svg>
  <div class="brand brand--back">
    <span class="brand__name"><span>Steadfast</span><span>Vermin</span><span>Guard</span></span>
    <span class="brand__mark"></span>
  </div>

  <h1 class="holder"><span class="holder__first">Gavin</span> <span class="holder__last">Holloway</span></h1>

  <p class="contact contact--phone">
    <svg viewBox="0 0 10 10" aria-hidden="true"><circle cx="5" cy="5" r="5" fill="var(--yellow)"/><path d="M3.2,2.6 L4.2,3.6 L3.7,4.3 Q4.4,5.6 5.7,6.3 L6.4,5.8 L7.4,6.8 L6.6,7.6 Q4.4,7.4 2.4,3.4 Z" fill="var(--ink)"/></svg>
    0461 275 804
  </p>
  <p class="contact contact--email">
    <svg viewBox="0 0 10 10" aria-hidden="true"><circle cx="5" cy="5" r="5" fill="var(--yellow)"/><rect x="2.6" y="3.4" width="4.8" height="3.4" fill="var(--ink)"/><path d="M2.6,3.4 L5,5.3 L7.4,3.4" fill="none" stroke="var(--yellow)" stroke-width="0.5"/></svg>
    Info@steadfastverminguard.com.au
  </p>

  <p class="services">
    Termites<span class="sep">|</span>Wood Borers<span class="sep">|</span>Ants<span class="sep">|</span>Cockroaches<span class="sep">|</span>Spiders<br>
    Fleas<span class="sep">|</span>Mice<span class="sep">|</span>Rats<span class="sep">|</span>Bed Bugs &amp; More!
  </p>
</section>

</body>
</html>
```